Trailer Lettering or Partial Wrap

I purchased a new gloss black 7' wide x 12' long x 7' height enclosed cargo trailer that I would like to brand for advertising. on all 4 sides. Our font is AgencyFB (and we only use lower case letters). To reduce cost I thought using the black gloss background could be achieved and use cut out vinyl rather than full wrap unless there are some other ideas. Our colors are Black, White, and Red (HEX #BE1E2D. Items to be displayed:
- logo
- phone # (405) 555-0147
- email. catering@thekelpdockok.com
- web address: www.thekelpdockok.com
- our 2 restaurant locations
- "Edmond" 4870 SE 52nd, Edmond OK 73025
- "NW-OKC" 2915 E Larkspur Rd, Oklahoma City, OK 73159

we would also like to highlight 3 services we offer:
- Catering
- Rent-A-Chef Events
- Sushi Making Classes

For reference our chopsticks from the logo files we use on a lot of print items. Not that I want it to be like this, but I did attach a sample of what ChatGPT created though is in an unusable format and fonts aren't consistent. As well a recent 2' x 4' sign we had made to use on table displays.

We also do like the wording on that last item of " Sushi | Experience | Elevated"

```html
<!DOCTYPE html>
<html lang="en">
<head>
<meta charset="utf-8">
<title>the kelp dock — trailer lettering</title>
<link rel="stylesheet" href="https://fonts.googleapis.com/css2?family=Saira+Extra+Condensed:wght@400;500&display=swap">
<style>
  :root {
    --bg: #cfcfcf;
    --panel: #050505;
    --red: #be1e2d;
    --white: #ffffff;
    --frame: #e6e6e6;
  }
  * { box-sizing: border-box; margin: 0; padding: 0; }
  html, body { width: 1200px; height: 1001px; overflow: hidden; background: var(--bg); }
  body { font-family: "Saira Extra Condensed", "Arial Narrow", "Roboto Condensed", sans-serif; color: var(--white); position: relative; }
  p, li, span { white-space: nowrap; }

  .panel { position: absolute; background: var(--panel); overflow: hidden; }
  .panel--rear { left: 20px; top: 330px; width: 340px; height: 340px; }
  .panel--side { left: 380px; top: 272px; width: 800px; height: 460px; }

  .brand { position: absolute; border: 5px solid var(--red); border-radius: 50%;
    display: flex; align-items: center; justify-content: center; text-align: center;
    font-weight: 500; line-height: 0.88; color: var(--white); }
  .brand--side { left: 30px; top: 28px; width: 200px; height: 200px; font-size: 50px; }
  .brand--rear { left: 115px; top: 16px; width: 110px; height: 110px; font-size: 27px; }
  .brand--door { left: 16px; top: 140px; width: 88px; height: 88px; font-size: 21px; }

  .icon { width: 46px; height: 46px; flex: none; }
  .icon .ring { fill: none; stroke: var(--red); stroke-width: 3; }
  .icon .glyph { fill: none; stroke: var(--white); stroke-width: 1.8; stroke-linejoin: round; stroke-linecap: round; }

  .services { position: absolute; left: 250px; top: 36px; width: 160px; list-style: none; }
  .service { display: flex; align-items: center; gap: 10px; height: 84px; border-bottom: 1px solid var(--red); }
  .service:last-child { border-bottom: none; }
  .service__label { font-size: 16px; line-height: 1.05; }

  .tagline { position: absolute; left: 432px; top: 60px; list-style: none; }
  .tagline li { font-size: 34px; line-height: 1; padding-left: 10px; border-left: 3px solid var(--red); margin-bottom: 12px; }

  .door { position: absolute; left: 652px; top: 115px; width: 124px; height: 345px; border: 7px solid var(--frame); border-bottom: none; background: var(--panel); }

  .rule { position: absolute; height: 2px; background: var(--red); }
  .panel--side .rule { left: 24px; top: 318px; width: 600px; }

  .location { position: absolute; top: 340px; font-size: 16px; line-height: 1.3; }
  .location--edmond { left: 24px; }
  .location--nwokc { left: 172px; }
  .location__name { color: var(--red); display: block; font-size: 18px; }

  .contact { position: absolute; display: flex; align-items: center; gap: 8px; line-height: 1; }
  .contact svg { flex: none; }
  .contact .ring { fill: none; stroke: var(--red); stroke-width: 2; }
  .contact .glyph { fill: none; stroke: var(--white); stroke-width: 1.6; stroke-linejoin: round; stroke-linecap: round; }
  .panel--side .contact--phone { left: 372px; top: 344px; font-size: 24px; }
  .panel--side .contact--email { left: 372px; top: 382px; font-size: 18px; }

  .web { position: absolute; background: var(--red); color: var(--white); text-align: center; line-height: 1; white-space: nowrap; }
  .panel--side .web { left: 372px; top: 418px; width: 260px; padding: 4px 0; font-size: 20px; }

  .panel--rear .contact--phone { left: 36px; top: 138px; font-size: 30px; }
  .panel--rear .contact--email { left: 36px; top: 182px; font-size: 17px; }
  .panel--rear .web { left: 36px; top: 210px; width: 250px; padding: 3px 0; font-size: 17px; }
  .panel--rear .rule { left: 24px; top: 246px; width: 292px; height: 1px; }

  .service-row { position: absolute; left: 20px; top: 256px; width: 300px; display: flex; justify-content: space-between; list-style: none; }
  .service-row li { width: 100px; display: flex; flex-direction: column; align-items: center; text-align: center; gap: 4px; font-size: 14px; line-height: 1.05; }
  .service-row .icon { width: 40px; height: 40px; }
</style>
</head>
<body>

<section class="panel panel--rear" aria-label="Rear panel">
  <div class="brand brand--rear">the<br>kelp<br>dock</div>
  <p class="contact contact--phone">
    <svg width="18" height="18" viewBox="0 0 18 18"><circle class="ring" cx="9" cy="9" r="8"/><path class="glyph" d="M6 5l2 2-1 1a5 5 0 0 0 3 3l1-1 2 2-1 1a7 7 0 0 1-7-7z"/></svg>
    <span>(405) 555-0147</span></p>
  <p class="contact contact--email">
    <svg width="16" height="16" viewBox="0 0 18 18"><circle class="ring" cx="9" cy="9" r="8"/><path class="glyph" d="M5 6h8v6H5zM5 6l4 3 4-3"/></svg>
    <span>catering@thekelpdockok.com</span></p>
  <p class="web">www.thekelpdockok.com</p>
  <div class="rule"></div>
  <ul class="service-row">
    <li><svg class="icon" viewBox="0 0 46 46"><circle class="ring" cx="23" cy="23" r="20"/><path class="glyph" d="M13 28h20M15 28a8 8 0 0 1 16 0M23 18v2"/></svg>catering</li>
    <li><svg class="icon" viewBox="0 0 46 46"><circle class="ring" cx="23" cy="23" r="20"/><path class="glyph" d="M17 26v5h12v-5M17 26a4 4 0 0 1 1-8a5 5 0 0 1 10 0a4 4 0 0 1 1 8z"/></svg>rent-a-chef<br>events</li>
    <li><svg class="icon" viewBox="0 0 46 46"><circle class="ring" cx="23" cy="23" r="20"/><path class="glyph" d="M12 22v7a5 2 0 0 0 10 0v-7M12 22a5 2 0 0 0 10 0a5 2 0 0 0-10 0M24 18v7a5 2 0 0 0 10 0v-7M24 18a5 2 0 0 0 10 0a5 2 0 0 0-10 0"/></svg>sushi making<br>classes</li>
  </ul>
</section>

<section class="panel panel--side" aria-label="Side panel">
  <div class="brand brand--side">the<br>kelp<br>dock</div>

  <ul class="services">
    <li class="service"><svg class="icon" viewBox="0 0 46 46"><circle class="ring" cx="23" cy="23" r="20"/><path class="glyph" d="M13 28h20M15 28a8 8 0 0 1 16 0M23 18v2"/></svg><span class="service__label">catering</span></li>
    <li class="service"><svg class="icon" viewBox="0 0 46 46"><circle class="ring" cx="23" cy="23" r="20"/><path class="glyph" d="M17 26v5h12v-5M17 26a4 4 0 0 1 1-8a5 5 0 0 1 10 0a4 4 0 0 1 1 8z"/></svg><span class="service__label">rent-a-chef<br>events</span></li>
    <li class="service"><svg class="icon" viewBox="0 0 46 46"><circle class="ring" cx="23" cy="23" r="20"/><path class="glyph" d="M12 22v7a5 2 0 0 0 10 0v-7M12 22a5 2 0 0 0 10 0a5 2 0 0 0-10 0M24 18v7a5 2 0 0 0 10 0v-7M24 18a5 2 0 0 0 10 0a5 2 0 0 0-10 0"/></svg><span class="service__label">sushi making<br>classes</span></li>
  </ul>

  <ul class="tagline">
    <li>sushi</li>
    <li>experience</li>
    <li>elevated</li>
  </ul>

  <div class="door">
    <div class="brand brand--door">the<br>kelp<br>dock</div>
  </div>

  <div class="rule"></div>

  <p class="location location--edmond"><span class="location__name">Edmond</span>4870 SE 52nd,<br>Edmond, OK 73025</p>
  <p class="location location--nwokc"><span class="location__name">NW-OKC</span>2915 E Larkspur Rd,<br>Oklahoma City, OK 73159</p>

  <p class="contact contact--phone">
    <svg width="22" height="22" viewBox="0 0 18 18"><circle class="ring" cx="9" cy="9" r="8"/><path class="glyph" d="M6 5l2 2-1 1a5 5 0 0 0 3 3l1-1 2 2-1 1a7 7 0 0 1-7-7z"/></svg>
    <span>(405) 555-0147</span></p>
  <p class="contact contact--email">
    <svg width="22" height="22" viewBox="0 0 18 18"><circle class="ring" cx="9" cy="9" r="8"/><path class="glyph" d="M5 6h8v6H5zM5 6l4 3 4-3"/></svg>
    <span>catering@thekelpdockok.com</span></p>
  <p class="web">www.thekelpdockok.com</p>
</section>

</body>
</html>
```